Hollowbrook Renderworks Wordpress Design

I would like a design for my friends company. He has just had his logo designed and really likes the following website.

www.tbr-skimcoat.co.uk

Something similar to this design would be ideal but open to additional ideas. The website shown has all the relevant content.

We have 20 years of experience and can provide a number of photos for work we have done.

More photos will be provided upon request.

Target Market(s)

Homeowners

Industry/Entity Type

Trade

Font styles to use
Sans Serif

Colors
3176b5
85cae6
85abd2
eaf1f7

Requirements
Must have
• look at www.tbr-skimcoat.co.uk
Nice to have
Should not have
• N/A

```html
<!DOCTYPE html>
<html lang="en">
<head>
<meta charset="utf-8">
<title>Hollowbrook Renderworks</title>
<link rel="stylesheet" href="https://fonts.googleapis.com/css2?family=Open+Sans:wght@400;600;700&family=Crimson+Text:wght@400&display=swap">
<style>
:root{
  --blue:#3176b5;
  --sky:#85cae6;
  --soft:#85abd2;
  --mist:#eaf1f7;
  --ink:#222;
  --grey:#555;
  --white:#fff;
}
*{box-sizing:border-box;margin:0;padding:0}
html,body{width:1200px;height:1200px;overflow:hidden;background:var(--white);font-family:"Open Sans",sans-serif;color:var(--ink)}
.page{width:1200px;height:1200px;overflow:hidden;position:relative}

.topbar{height:36px;background:var(--blue);color:var(--white);font-size:12px;display:flex;align-items:center;justify-content:space-between;padding:0 180px 0 170px}
.topbar .contact{display:flex;gap:18px;align-items:center}
.topbar .contact span{display:flex;align-items:center;gap:7px}
.topbar .social{display:flex;height:36px}
.topbar .social i{width:30px;height:36px;border-left:1px solid rgba(255,255,255,.25);display:flex;align-items:center;justify-content:center}
.topbar .social i:last-child{border-right:1px solid rgba(255,255,255,.25)}
.topbar .social i::after{content:"";width:9px;height:9px;background:var(--white);border-radius:1px}

.header{height:75px;display:flex;align-items:center;justify-content:space-between;padding:0 180px 0 168px;background:var(--white)}
.logo{display:flex;align-items:center;gap:8px;color:var(--blue);font-weight:600;font-size:16px;letter-spacing:.4px;white-space:nowrap}
.logo .mark{width:11px;height:11px;background:var(--blue)}
.nav{display:flex;gap:26px;font-size:11px;font-weight:600;letter-spacing:.4px;white-space:nowrap}
.nav a{color:#333;text-decoration:none}
.nav a.active{color:var(--blue)}

.hero{height:410px;display:flex;background:var(--blue)}
.hero .photo{width:668px;height:410px;background:linear-gradient(160deg,#9cc4ec 0%,#a89a86 38%,#7d6c58 70%,#5e5144 100%)}
.hero .form{flex:1;padding:30px 0 0 15px;color:var(--white)}
.hero h1{font-family:"Crimson Text",serif;font-weight:400;font-size:23px;letter-spacing:.3px;line-height:1.2}
.hero .lead{font-family:"Crimson Text",serif;font-size:19px;line-height:1.2;margin-top:2px}
.field{margin-top:12px}
.field label{font-size:11px;display:block;margin-bottom:5px}
.field .input{width:357px;height:28px;background:var(--white)}
.submit{margin-top:18px;display:inline-block;background:var(--sky);color:var(--blue);font-weight:700;font-size:14px;padding:7px 16px;letter-spacing:.3px}
.callnow{margin-top:22px;font-weight:700;font-size:20px}
.callnow span{color:var(--sky)}

.services{padding:20px 0 22px;text-align:center}
.section-title{font-size:22px;font-weight:400;letter-spacing:.5px;line-height:1.2}
.section-title::after{content:"";display:block;width:86px;height:2px;background:var(--blue);margin:10px auto 0}
.grid{width:896px;margin:16px auto 0;display:grid;grid-template-columns:repeat(3,1fr);row-gap:16px}
.card .icon{width:66px;height:66px;border-radius:50%;background:var(--sky);margin:0 auto;display:flex;align-items:center;justify-content:center}
.card .stem{width:1px;height:8px;background:var(--sky);margin:0 auto}
.card .dot{width:7px;height:7px;border:1px solid var(--sky);border-radius:50%;margin:0 auto}
.card h3{font-size:12.5px;font-weight:600;letter-spacing:.3px;margin-top:10px;line-height:1.3}
.card p{font-size:10px;line-height:1.45;color:var(--grey);margin:7px auto 0;width:280px}

.about{background:var(--blue);color:var(--white);text-align:center;padding-top:18px;height:400px}
.about h2{font-size:22px;font-weight:400;letter-spacing:.5px;line-height:1.2}
.about .sub{font-size:13px;margin-top:12px;color:var(--mist)}
.about .body{display:flex;gap:16px;width:880px;margin:18px auto 0;text-align:left}
.video{width:430px;height:220px;border:2px solid var(--white);background:linear-gradient(180deg,#8a8478 0%,#b9b2a6 55%,#6e675c 100%);position:relative;flex:none}
.video .play{position:absolute;left:50%;top:40%;transform:translate(-50%,-50%)}
.about .text p{font-size:11px;line-height:1.45;margin-bottom:12px}
</style>
</head>
<body>
<div class="page">
  <div class="topbar">
    <div class="contact">
      <span><svg width="11" height="11" viewBox="0 0 24 24"><path fill="#fff" d="M6.6 10.8a15 15 0 006.6 6.6l2.2-2.2c.3-.3.7-.4 1-.2 1.1.4 2.3.6 3.6.6.6 0 1 .4 1 1V20c0 .6-.4 1-1 1A17 17 0 013 4c0-.6.4-1 1-1h3.5c.6 0 1 .4 1 1 0 1.3.2 2.5.6 3.6.1.3 0 .7-.2 1z"/></svg>555-014-7290</span>
      <span><svg width="12" height="10" viewBox="0 0 24 18"><rect x="1" y="1" width="22" height="16" fill="none" stroke="#fff" stroke-width="2"/><path d="M1 1l11 9 11-9" fill="none" stroke="#fff" stroke-width="2"/></svg>info@hollowbrookrenderworks.com</span>
    </div>
    <div class="social"><i></i><i></i><i></i><i></i></div>
  </div>

  <header class="header">
    <div class="logo"><span class="mark"></span>HOLLOWBROOK RENDERWORKS</div>
    <nav class="nav">
      <a href="#">HOME</a><a href="#" class="active">SERVICES</a><a href="#">PRODUCTS</a><a href="#">FREE ESTIMATE</a><a href="#">TESTIMONIALS</a><a href="#">BLOG</a><a href="#">CONTACT</a>
    </nav>
  </header>

  <section class="hero">
    <div class="photo" role="img" aria-label="Photo of a stone house under renovation against a blue sky"></div>
    <div class="form">
      <h1>WELCOME TO OUR COMPANY</h1>
      <div class="lead">Let us call you, just fill in the boxes below!</div>
      <div class="field"><label>Full Name*</label><div class="input"></div></div>
      <div class="field"><label>Phone Number</label><div class="input"></div></div>
      <div class="field"><label>Email Address*</label><div class="input"></div></div>
      <div class="submit">SUBMIT NOW</div>
      <div class="callnow">CALL NOW <span>555 318 0426</span></div>
    </div>
  </section>

  <section class="services">
    <h2 class="section-title">OUR OTHER SERVICE</h2>
    <div class="grid">
      <div class="card">
        <div class="icon"><svg width="30" height="34" viewBox="0 0 34 38"><rect x="4" y="4" width="22" height="9" rx="2" fill="#fff"/><rect x="14" y="13" width="3" height="8" fill="#fff"/><rect x="12" y="21" width="7" height="15" rx="2" fill="#fff"/></svg></div>
        <div class="stem"></div><div class="dot"></div>
        <h3>SERVICES NAME</h3>
        <p>There are many variations of passages of Lorem Ipsum available, but the majority have suffered alteration in some form, by injected humour, or randomised words which don't look even slightly believable.</p>
      </div>
      <div class="card">
        <div class="icon"><svg width="36" height="32" viewBox="0 0 40 36"><path d="M20 2L2 17h5v17h26V17h5z" fill="#fff"/><rect x="11" y="20" width="6" height="6" fill="#85cae6"/><rect x="23" y="20" width="6" height="6" fill="#85cae6"/></svg></div>
        <div class="stem"></div><div class="dot"></div>
        <h3>SERVICES NAME HERE</h3>
        <p>Duskguard is a revolutionary bio sensor bed bug detection system that helps you determine once and for all if you have a bed bug infestation on your hands.</p>
      </div>
      <div class="card">
        <div class="icon"><svg width="30" height="34" viewBox="0 0 34 38"><rect x="6" y="4" width="22" height="9" rx="2" fill="#fff"/><rect x="16" y="13" width="3" height="8" fill="#fff"/><rect x="14" y="21" width="7" height="15" rx="2" fill="#fff"/></svg></div>
        <div class="stem"></div><div class="dot"></div>
        <h3>SERVICE NAME HERE</h3>
        <p>Stowsafe is available for shipping now. In fact if you are in the Toronto area we can deliver this product to you same day since we have inventory in stock!</p>
      </div>
      <div class="card">
        <div class="icon"><svg width="30" height="34" viewBox="0 0 34 38"><rect x="4" y="4" width="22" height="9" rx="2" fill="#fff"/><rect x="14" y="13" width="3" height="8" fill="#fff"/><rect x="12" y="21" width="7" height="15" rx="2" fill="#fff"/></svg></div>
        <div class="stem"></div><div class="dot"></div>
        <h3>SERVICES NAME</h3>
        <p>There are many variations of passages of Lorem Ipsum available, but the majority have suffered alteration in some form, by injected humour, or randomised words which don't look even slightly believable.</p>
      </div>
      <div class="card">
        <div class="icon"><svg width="36" height="32" viewBox="0 0 40 36"><path d="M20 2L2 17h5v17h26V17h5z" fill="#fff"/><rect x="11" y="20" width="6" height="6" fill="#85cae6"/><rect x="23" y="20" width="6" height="6" fill="#85cae6"/></svg></div>
        <div class="stem"></div><div class="dot"></div>
        <h3>SERVICES NAME HERE</h3>
        <p>Duskguard is a revolutionary bio sensor bed bug detection system that helps you determine once and for all if you have a bed bug infestation on your hands.</p>
      </div>
      <div class="card">
        <div class="icon"><svg width="30" height="34" viewBox="0 0 34 38"><rect x="6" y="4" width="22" height="9" rx="2" fill="#fff"/><rect x="16" y="13" width="3" height="8" fill="#fff"/><rect x="14" y="21" width="7" height="15" rx="2" fill="#fff"/></svg></div>
        <div class="stem"></div><div class="dot"></div>
        <h3>SERVICE NAME HERE</h3>
        <p>Stowsafe is available for shipping now. In fact if you are in the Toronto area we can deliver this product to you same day since we have inventory in stock!</p>
      </div>
    </div>
  </section>

  <section class="about">
    <h2>ABOUT OUR COMPANY</h2>
    <div class="sub">Toronto Bed Bugs Heat Treatment is a preferred solution over Chemicals?</div>
    <div class="body">
      <div class="video" role="img" aria-label="Video still of a bare interior room with timber beams during renovation">
        <svg class="play" width="48" height="48" viewBox="0 0 48 48"><circle cx="24" cy="24" r="23" fill="rgba(255,255,255,.9)"/><path d="M19 15l14 9-14 9z" fill="#3176b5"/></svg>
      </div>
      <div class="text">
        <p>There are many variations of passages of Lorem Ipsum available, but the majority have suffered alteration in some form, by injected humour, or randomised words which don't look even slightly believable. If you are going to use a passage of Lorem Ipsum.</p>
        <p>There are many variations of passages of Lorem Ipsum available, but the majority have suffered alteration in some form, by injected humour, or randomised words which don't look even slightly believable. If you are going to use a passage of Lorem Ipsum.</p>
      </div>
    </div>
  </section>
</div>
</body>
</html>
```